Dropper bottle label for sublingual NAD+ drops

Design label for a new NAD+ anti-aging supplement. The product name is Vessa which is Latin for youth. Would like small Coldmarsh label incorporated. Logo can be found at Coldmarsh Vitality Collective.com. Product is life changing and will be best on market. NAD+ is a coenzyme normally found in body. Must have to live. Restores cells at mitochondrial level. As close to fountain of youth as science knows today. Naturopathic not a drop. Raw ingredients and processing for Vessa will make it the top of the line for this type of product

Primarily for anti-aging. 45 plus

Script

Designer to choose colors to be used in the design.

• Must be simple and must gently incorporate logo. No pictures script for Vessa
• Bottle will be black so would like colors that go with it. Perhaps Vessa in larger black or outlined letters with NAD+ in blue. Logo in green
• Pictures

```html
<!DOCTYPE html>
<html lang="en">
<head>
<meta charset="utf-8">
<title>Vessa NAD+ Label</title>
<link rel="stylesheet" href="https://fonts.googleapis.com/css2?family=Source+Sans+3:wght@400;600;700;800&display=swap">
<style>
  :root {
    --page: #ffffff;
    --label: #eceeef;
    --label-edge: #dcdfe1;
    --ink: #1b1b1d;
    --blue: #1e6fbf;
    --blue-light: #cfe3f6;
    --green: #2f9a6b;
  }
  * { margin: 0; padding: 0; box-sizing: border-box; }
  html, body {
    width: 1200px;
    height: 1200px;
    overflow: hidden;
    background: var(--page);
  }
  .canvas {
    width: 1200px;
    height: 1200px;
    display: flex;
    align-items: center;
    justify-content: center;
  }
  .label {
    width: 640px;
    height: 900px;
    background: linear-gradient(90deg, var(--label-edge) 0%, var(--label) 18%, #f4f5f6 50%, var(--label) 82%, var(--label-edge) 100%);
    display: flex;
    flex-direction: column;
    align-items: center;
    padding-top: 110px;
    font-family: "Source Sans 3", sans-serif;
    color: var(--ink);
  }
  .brand-mark {
    display: flex;
    align-items: center;
    gap: 14px;
    color: var(--green);
    font-weight: 600;
    font-size: 34px;
    letter-spacing: 2px;
  }
  .brand-mark .dot {
    width: 16px;
    height: 16px;
    border-radius: 50%;
    background: var(--green);
  }
  .product-name {
    margin-top: 150px;
    font-family: "Source Sans 3", sans-serif;
    font-weight: 700;
    font-size: 150px;
    line-height: 1;
    letter-spacing: 10px;
    color: var(--ink);
  }
  .product-type {
    margin-top: 20px;
    font-weight: 800;
    font-size: 116px;
    line-height: 1;
    color: var(--blue);
  }
  .claim {
    margin-top: 18px;
    background: var(--blue);
    color: var(--blue-light);
    font-weight: 600;
    font-size: 30px;
    letter-spacing: 0.5px;
    padding: 4px 22px;
    border-radius: 12px;
  }
  .supply {
    margin-top: 26px;
    font-weight: 600;
    font-size: 40px;
  }
  .rule {
    margin-top: 22px;
    width: 100%;
    height: 10px;
    background: var(--blue);
  }
  .volume {
    margin-top: 30px;
    font-weight: 600;
    font-size: 28px;
  }
</style>
</head>
<body>
  <main class="canvas">
    <section class="label">
      <div class="brand-mark"><span class="dot"></span>Coldmarsh</div>
      <h1 class="product-name">VESSA</h1>
      <p class="product-type">NAD+</p>
      <p class="claim">ANTI-AGING SUPPLEMENT</p>
      <p class="supply">30 Day Supply</p>
      <div class="rule"></div>
      <p class="volume">1 fl oz. ( 30 ml )</p>
    </section>
  </main>
</body>
</html>
```